Business Card design for amazing new Dental Office

Please read this brief closely!

Our client is a modern new dental office/
They love their new logo.
Now it's time to create a business card for them.

It should be a two sided card:
Side one should have the logo and name and maybe a color background or design.
Side two should have all the contact information which is here:

Marcus Pellow, D.D.S
General and Cosmetic Dentistry
4178 W. Orchard Lane
Ventura, CA 93017
(805) 219-4862
drmarc@bluefernsmiles.example
www.bluefernsmiles.example

Feel free to arrange that info as you like and to style both sides of the card according to your creativity. This is a chance for you to show your design skills!

Client is open to font choices and is looking for a style that is amazing and premium. Colors can be selected from the logo, or any variation of those.

You will not win this contest with a less than beautiful card design so please feel free to make multiple submissions.

Logo files attached and please message me with any questions.
Thanks!

Target Market(s)

Families and Professionals seeking dental services

Industry/Entity Type

Dental

Contact Information for Business Card

Logo, style, contact info as per the brief

Font styles to use
Sans Serif

Requirements
Must have
• Client's logo and contact details as per brief
Nice to have
• Unique style reflecting high end dental clinic near the beach
Should not have
• Must not look like a template

```html
<!DOCTYPE html>
<html lang="en">
<head>
<meta charset="utf-8">
<title>Blue Fern Dental – Business Card</title>
<link href="https://fonts.googleapis.com/css2?family=Jost:wght@300;400&display=swap" rel="stylesheet">
<style>
  :root {
    --backdrop: #b9b9b9;
    --card-white: #ffffff;
    --card-dark: #303030;
    --sea-blue: #4ab4e8;
    --gold: #d4c24b;
    --wordmark-grey: #a3a3a3;
    --emboss: #262626;
    --ink-light: #ffffff;
  }
  * { margin: 0; padding: 0; box-sizing: border-box; }
  html, body { width: 1200px; height: 1200px; overflow: hidden; }
  body {
    background: var(--backdrop);
    font-family: "Jost", sans-serif;
    font-weight: 300;
    position: relative;
  }
  .card {
    position: absolute;
    left: 262px;
    width: 800px;
    height: 457px;
    transform: scale(0.8575);
    transform-origin: top left;
    overflow: hidden;
  }
  .card--front { top: 165px; background: var(--card-white); }
  .card--back { top: 653px; background: var(--card-dark); }

  .front-panel { position: absolute; inset: 0; width: 800px; height: 457px; }

  .wordmark {
    position: absolute;
    left: 40px;
    width: 360px;
    top: 90px;
    text-align: center;
    color: var(--wordmark-grey);
    font-weight: 300;
  }
  .wordmark__name { font-size: 40px; letter-spacing: 3px; line-height: 1; display: block; }
  .wordmark__sub { font-size: 19px; letter-spacing: 15px; line-height: 1; display: block; margin-top: 20px; padding-left: 15px; }

  .contact {
    position: absolute;
    right: 44px;
    top: 262px;
    text-align: right;
    color: var(--ink-light);
  }
  .contact__name { font-size: 27px; line-height: 1; font-weight: 300; }
  .contact__role { font-size: 18px; line-height: 1; margin-top: 9px; font-weight: 300; }
  .contact__lines { margin-top: 16px; font-size: 18px; font-weight: 300; }
  .contact__line { display: flex; justify-content: flex-end; align-items: center; gap: 6px; line-height: 22px; }
  .contact__line svg { width: 14px; height: 14px; fill: var(--ink-light); }
  .contact__address { margin-top: 10px; font-size: 19px; font-weight: 300; line-height: 1; }

  .back-mark {
    position: absolute;
    left: 0; right: 0;
    top: 150px;
    text-align: center;
    color: var(--emboss);
    font-size: 64px;
    font-weight: 400;
    letter-spacing: 6px;
  }
  .back-url {
    position: absolute;
    left: 0; right: 0;
    top: 388px;
    text-align: center;
    color: var(--ink-light);
    font-size: 20px;
    letter-spacing: 6px;
    font-weight: 400;
  }
</style>
</head>
<body>
  <section class="card card--front" aria-label="Card front">
    <svg class="front-panel" viewBox="0 0 800 457" aria-hidden="true">
      <line x1="0" y1="340" x2="800" y2="100" stroke="var(--gold)" stroke-width="6"/>
      <path fill="var(--sea-blue)" d="M0 360 L800 120 L800 457 L0 457 Z"/>
    </svg>

    <div class="wordmark">
      <span class="wordmark__name">BLUE FERN</span>
      <span class="wordmark__sub">DENTAL</span>
    </div>

    <div class="contact">
      <p class="contact__name">Marcus Pellow, D.D.S</p>
      <p class="contact__role">General &amp; Cosmetic Dentistry</p>
      <div class="contact__lines">
        <p class="contact__line">(805) 219-4862
          <svg viewBox="0 0 16 16" aria-hidden="true"><path d="M3.5 1 L6 1 L7 4.5 L5.3 5.8 C6.2 7.8 8.2 9.8 10.2 10.7 L11.5 9 L15 10 L15 12.5 C15 13.9 13.9 15 12.5 15 C6.4 15 1 9.6 1 3.5 C1 2.1 2.1 1 3.5 1 Z"/></svg>
        </p>
        <p class="contact__line">drmarc@bluefernsmiles.example
          <svg viewBox="0 0 16 16" aria-hidden="true"><path d="M1 3 H15 V13 H1 Z M2.2 4.2 L8 8.6 L13.8 4.2 Z" fill-rule="evenodd"/></svg>
        </p>
        <p class="contact__line">www.bluefernsmiles.example
          <svg viewBox="0 0 16 16" aria-hidden="true"><circle cx="8" cy="8" r="7"/></svg>
        </p>
      </div>
      <p class="contact__address">4178 W. Orchard Lane, Ventura, CA 93017</p>
    </div>
  </section>

  <section class="card card--back" aria-label="Card back">
    <p class="back-mark">BLUE FERN</p>
    <p class="back-url">WWW.BLUEFERNSMILES.EXAMPLE</p>
  </section>
</body>
</html>
```